Motorcycle Shop Business Card

New business card for Motorcycle repair and customization shop.Business name: Copper Falcon Chris Morris443-865-5190, 7214 Quarry Lane Arbutus, MD 21227. www.dale@copperfalconcustoms.example. I uploaded some motorcycle images and logo and a couple of our calendar shoots. They do not have to be used on card just examples of some of our work and past graphic work.
We work on Vantor Brennick and Custom Built Motorcycles.

Looking for front and back design

Target Market(s)

Motorcycle owners

Industry/Entity Type

Motorcycle Part

```html
<!DOCTYPE html>
<html lang="en">
<head>
<meta charset="UTF-8">
<title>Copper Falcon Customs – Business Card</title>
<link rel="stylesheet" href="https://fonts.googleapis.com/css2?family=Poppins:wght@400;500;800&display=swap">
<style>
  :root {
    --backdrop: #ebebeb;
    --card-blue: #0a3cf5;
    --ink: #0a0a0a;
    --muted: #8c8c95;
    --studio-white: #ffffff;
    --studio-floor: #e4e6ea;
    --chrome: #b9bec6;
    --teal-paint: #9fd4d8;
    --red-paint: #8a1620;
    --blue-paint: #1c3aa8;
    --tire-black: #1a1a1a;
    --storm-dark: #17242c;
    --storm-mid: #4f6670;
    --storm-light: #b9c8cc;
    --wing-tan: #b08a68;
    --mono-dark: #1e1e1e;
    --mono-mid: #5a5a5a;
    --mono-light: #a8a8a8;
    --haze-grey: #8d8d8d;
    --haze-white: #f4f4f4;
  }
  * { box-sizing: border-box; margin: 0; padding: 0; }
  html, body {
    width: 1200px; height: 1200px; overflow: hidden;
    background: var(--backdrop);
    font-family: "Poppins", sans-serif;
  }
  .canvas { position: relative; width: 1200px; height: 1200px; }
  .card {
    position: absolute; left: 160px; width: 880px; height: 503px;
    background: var(--card-blue);
    box-shadow: 0 10px 24px rgba(0,0,0,0.18);
  }
  .card--portfolio { top: 70px; padding: 32px; }
  .card--contact { top: 627px; }

  .portfolio-grid {
    display: grid;
    grid-template-columns: repeat(3, 1fr);
    grid-template-rows: repeat(2, 1fr);
    gap: 10px;
    width: 100%; height: 100%;
  }
  .work-tile { width: 100%; height: 100%; }

  /* studio shots: bright white sweep, soft floor shadow, paint tone in the middle */
  .work-tile--teal-bike {
    background:
      radial-gradient(ellipse 42% 22% at 50% 72%, rgba(30,30,30,0.35), transparent 70%),
      radial-gradient(ellipse 34% 26% at 38% 52%, var(--teal-paint), transparent 75%),
      radial-gradient(ellipse 46% 30% at 55% 50%, var(--chrome), transparent 75%),
      linear-gradient(180deg, var(--studio-white) 0%, var(--studio-white) 55%, var(--studio-floor) 100%);
  }
  .work-tile--red-bike {
    background:
      radial-gradient(ellipse 42% 20% at 52% 74%, rgba(30,30,30,0.35), transparent 70%),
      radial-gradient(ellipse 28% 24% at 48% 48%, var(--red-paint), transparent 75%),
      radial-gradient(ellipse 30% 26% at 34% 55%, var(--tire-black), transparent 72%),
      radial-gradient(ellipse 48% 32% at 55% 50%, var(--chrome), transparent 75%),
      linear-gradient(180deg, var(--studio-white) 0%, var(--studio-white) 55%, var(--studio-floor) 100%);
  }
  .work-tile--blue-bike {
    background:
      radial-gradient(ellipse 42% 20% at 50% 76%, rgba(30,30,30,0.35), transparent 70%),
      radial-gradient(ellipse 30% 26% at 42% 54%, var(--blue-paint), transparent 75%),
      radial-gradient(ellipse 22% 22% at 78% 46%, var(--blue-paint), transparent 72%),
      radial-gradient(ellipse 48% 32% at 55% 52%, var(--chrome), transparent 75%),
      linear-gradient(180deg, var(--studio-white) 0%, var(--studio-white) 55%, var(--studio-floor) 100%);
  }
  .work-tile--storm {
    background:
      radial-gradient(ellipse 30% 22% at 52% 56%, var(--wing-tan), transparent 75%),
      radial-gradient(ellipse 55% 35% at 45% 35%, var(--storm-light), transparent 70%),
      radial-gradient(ellipse 70% 60% at 50% 50%, var(--storm-mid), transparent 80%),
      var(--storm-dark);
  }
  .work-tile--garage {
    background:
      radial-gradient(ellipse 35% 30% at 40% 45%, var(--mono-light), transparent 75%),
      radial-gradient(ellipse 50% 40% at 60% 60%, var(--mono-mid), transparent 80%),
      linear-gradient(160deg, var(--mono-mid), var(--mono-dark));
  }
  .work-tile--haze {
    background:
      radial-gradient(ellipse 34% 26% at 58% 60%, var(--tire-black), transparent 72%),
      radial-gradient(ellipse 45% 35% at 40% 35%, var(--haze-white), transparent 70%),
      linear-gradient(180deg, var(--haze-grey) 0%, #c4c4c4 60%, var(--haze-white) 100%);
  }

  .brand {
    position: absolute; left: 110px; top: 190px; width: 330px;
    display: flex; align-items: center; gap: 16px;
    color: var(--ink);
  }
  .brand-mark { width: 28px; height: 28px; flex: none; background: var(--ink); }
  .brand-name {
    font-weight: 800; font-size: 36px; line-height: 1.05; text-transform: uppercase;
  }
  .divider {
    position: absolute; left: 470px; top: 80px; width: 2px; height: 340px;
    background: var(--muted); opacity: 0.8;
  }
  .contact-block {
    position: absolute; left: 505px; top: 130px; width: 350px; color: var(--ink);
  }
  .person-name {
    font-weight: 800; font-size: 38px; line-height: 1; text-transform: uppercase;
    margin-bottom: 26px; letter-spacing: -0.5px; white-space: nowrap;
  }
  .contact-list { list-style: none; }
  .contact-item {
    display: flex; align-items: flex-start; gap: 12px;
    font-size: 14px; font-weight: 500; line-height: 1.3;
    margin-bottom: 12px; white-space: nowrap;
  }
  .contact-icon { width: 20px; height: 20px; flex: none; }
  .contact-icon path, .contact-icon circle, .contact-icon rect { fill: var(--muted); }
  .contact-icon .stroke { fill: none; stroke: var(--muted); stroke-width: 2; }
  .contact-icon .cutout { fill: none; stroke: var(--card-blue); stroke-width: 1.6; }
</style>
</head>
<body>
<main class="canvas">

  <section class="card card--portfolio" aria-label="Card front: portfolio of custom work">
    <div class="portfolio-grid">
      <div class="work-tile work-tile--teal-bike" role="img" aria-label="Studio photo of a custom chopper with pale teal paint and chrome on white"></div>
      <div class="work-tile work-tile--storm" role="img" aria-label="Calendar illustration of a winged figure against a stormy night sky"></div>
      <div class="work-tile work-tile--red-bike" role="img" aria-label="Studio photo of a black and red custom bike on white"></div>
      <div class="work-tile work-tile--garage" role="img" aria-label="Black and white calendar shoot among bikes in the workshop"></div>
      <div class="work-tile work-tile--blue-bike" role="img" aria-label="Studio photo of a blue custom chopper with chrome on white"></div>
      <div class="work-tile work-tile--haze" role="img" aria-label="Calendar shoot with a black custom bike in grey haze"></div>
    </div>
  </section>

  <section class="card card--contact" aria-label="Card back: contact details">
    <div class="brand">
      <span class="brand-mark" aria-hidden="true"></span>
      <span class="brand-name">Copper Falcon Customs</span>
    </div>

    <div class="divider" aria-hidden="true"></div>

    <div class="contact-block">
      <h1 class="person-name">Dale Fenwick</h1>
      <ul class="contact-list">
        <li class="contact-item">
          <svg class="contact-icon" viewBox="0 0 20 20" aria-hidden="true"><path d="M5 2h3l1.5 4-2 1.5a10 10 0 0 0 5 5L14 10.5l4 1.5v3a2 2 0 0 1-2 2C8 17 3 12 3 4a2 2 0 0 1 2-2z"/></svg>
          <span>410-555-0137</span>
        </li>
        <li class="contact-item">
          <svg class="contact-icon" viewBox="0 0 20 20" aria-hidden="true"><rect x="2" y="4" width="16" height="12" rx="1"/><path d="M2.5 5l7.5 6 7.5-6" class="cutout"/></svg>
          <span>dale@copperfalconcustoms.example</span>
        </li>
        <li class="contact-item">
          <svg class="contact-icon" viewBox="0 0 20 20" aria-hidden="true"><circle cx="10" cy="10" r="7.5" class="stroke"/><path d="M2.5 10h15M10 2.5c3 3 3 12 0 15M10 2.5c-3 3-3 12 0 15" class="stroke"/></svg>
          <span>www.copperfalconcustoms.example</span>
        </li>
        <li class="contact-item">
          <svg class="contact-icon" viewBox="0 0 20 20" aria-hidden="true"><path d="M10 1a6 6 0 0 0-6 6c0 4.5 6 12 6 12s6-7.5 6-12a6 6 0 0 0-6-6zm0 8.5A2.5 2.5 0 1 1 10 4.5a2.5 2.5 0 0 1 0 5z"/></svg>
          <span>7214 QUARRY LANE ARBUTUS,<br>MD 21227.</span>
        </li>
      </ul>
    </div>
  </section>

</main>
</body>
</html>
```